Need Business Cards, Letterhead, and Stationary

Hi, please design a full stationary set for the attached logo (Business Cards, Letterhead, A4 Envelope, and other important stationary items that you can think of)
Please be as creative as you wish. The logo is for An Entrepreneurship Academy that teaches young and starting Entrepreneur skills they need to start their business.
Business
Serif
Sans Serif

```html
<!DOCTYPE html>
<html lang="en">
<head>
<meta charset="utf-8">
<title>Kernel Founders Academy – Stationery Set</title>
<link rel="stylesheet" href="https://fonts.googleapis.com/css2?family=Arimo:wght@400;700&display=swap">
<style>
  :root{
    --ink:#1c1c1c;
    --blue:#1f78ad;
    --yellow:#f6c400;
    --grey:#6d6e70;
    --card-dark:#58595b;
    --paper:#ffffff;
    --text:#333333;
    --bg-light:#c9c9c9;
    --bg-dark:#5a5a5a;
  }
  *{box-sizing:border-box;margin:0;padding:0}
  html,body{width:1200px;height:942px;overflow:hidden}
  body{
    font-family:"Arimo",Arial,sans-serif;
    color:var(--text);
    background:linear-gradient(135deg,var(--bg-dark) 0%,#8e8e8e 40%,var(--bg-light) 100%);
    position:relative;
  }
  .sheet{position:absolute;background:var(--paper);box-shadow:0 2px 6px rgba(0,0,0,.35);overflow:hidden}

  /* brand name block */
  .brand{display:flex;align-items:center;gap:6px;font-weight:700;color:var(--text);letter-spacing:.5px;white-space:nowrap}
  .brand-dot{border-radius:50%;background:var(--text);flex:none}

  /* colour bands */
  .band{position:absolute;display:flex}
  .band span{flex:1}
  .b-ink{background:var(--ink)} .b-blue{background:var(--blue)} .b-yellow{background:var(--yellow)} .b-grey{background:var(--grey)}

  /* corner symbol area */
  .corner-mark{position:absolute;right:0;bottom:0;
    background:linear-gradient(135deg,var(--yellow) 0%,var(--yellow) 35%,var(--blue) 60%,var(--grey) 100%);
    clip-path:polygon(100% 0,100% 100%,0 100%)}
  .corner-mark.top{top:0;bottom:auto;clip-path:polygon(0 0,100% 0,100% 100%)}

  .contact{list-style:none;font-size:9px;line-height:1.35;white-space:nowrap}
  .contact li{display:flex;align-items:center;gap:4px}
  .ico{width:7px;height:7px;flex:none}

  /* letterhead */
  .letterhead{left:38px;top:40px;width:519px;height:670px}
  .letterhead .brand{position:absolute;left:34px;top:36px;font-size:26px}
  .letterhead .brand-dot{width:18px;height:18px}
  .letterhead .contact{position:absolute;right:28px;top:40px}
  .letterhead .band.top{right:0;top:0;width:150px;height:7px}
  .letterhead .band.bottom{left:0;bottom:0;width:100%;height:7px}
  .letterhead .corner-mark{width:140px;height:148px;bottom:7px}
  .letterhead .footer-line{position:absolute;left:166px;bottom:16px;font-size:9px}
  .letterhead .footer-line span{margin-left:14px}

  /* envelope */
  .envelope{left:592px;top:40px;width:558px;height:275px}
  .envelope .band.top{left:0;top:0;width:100%;height:9px}
  .envelope .band.bottom{left:0;bottom:0;width:100%;height:8px}
  .envelope .ident{position:absolute;left:34px;top:77px}
  .envelope .brand{font-size:22px;margin-bottom:6px}
  .envelope .brand-dot{width:15px;height:15px}
  .envelope .contact{font-size:8px}
  .envelope .corner-mark{width:94px;height:94px;bottom:8px}

  /* business cards */
  .card-front{left:592px;top:370px;width:273px;height:157px}
  .card-front .ident{position:absolute;left:18px;top:58px}
  .card-front .brand{font-size:22px;margin-bottom:8px}
  .card-front .brand-dot{width:15px;height:15px}
  .card-front .contact{font-size:8.5px;color:#222}
  .card-front .corner-mark{width:92px;height:92px}

  .card-back{left:888px;top:370px;width:274px;height:157px;background:var(--card-dark);color:#fff}
  .card-back .corner-mark{width:100px;height:100px;
    background:linear-gradient(135deg,#ffffff 0%,#e6e6e6 100%);clip-path:polygon(0 0,100% 0,0 100%);left:0;top:0}
  .card-back .holder{position:absolute;right:22px;top:14px;text-align:left}
  .card-back .holder-name{font-size:15px;font-weight:700}
  .card-back .holder-role{font-size:8px;margin-top:2px}
  .card-back .contact{position:absolute;left:22px;bottom:14px;color:#fff}
</style>
</head>
<body>

  <section class="sheet letterhead" aria-label="Letterhead">
    <div class="band top"><span class="b-ink"></span><span class="b-blue"></span><span class="b-yellow"></span><span class="b-ink"></span></div>
    <div class="brand"><span class="brand-dot"></span>KERNEL</div>
    <ul class="contact">
      <li><svg class="ico" viewBox="0 0 8 8"><rect x="2" y="0" width="4" height="8" rx="1" fill="var(--blue)"/></svg>0-000-000-0000</li>
      <li><svg class="ico" viewBox="0 0 8 8"><rect x="0" y="1" width="8" height="6" fill="var(--blue)"/></svg>mara@kernelmail.org</li>
      <li><svg class="ico" viewBox="0 0 8 8"><circle cx="4" cy="4" r="4" fill="var(--blue)"/></svg>www.website.com</li>
    </ul>
    <div class="corner-mark" role="img" aria-label="Large brand symbol decoration"></div>
    <p class="footer-line">www.website.com.<span>Address: 2/114Lorem Ipsum,</span></p>
    <div class="band bottom"><span class="b-grey"></span><span class="b-blue"></span><span class="b-yellow"></span><span class="b-ink"></span></div>
  </section>

  <section class="sheet envelope" aria-label="Envelope">
    <div class="band top"><span class="b-ink"></span><span class="b-blue"></span><span class="b-yellow"></span><span class="b-ink"></span></div>
    <div class="ident">
      <div class="brand"><span class="brand-dot"></span>KERNEL</div>
      <ul class="contact">
        <li>Kernel Founders Academy</li>
        <li><svg class="ico" viewBox="0 0 8 8"><rect x="2" y="0" width="4" height="8" rx="1" fill="var(--blue)"/></svg>0-000-000-0000</li>
        <li><svg class="ico" viewBox="0 0 8 8"><rect x="0" y="1" width="8" height="6" fill="var(--blue)"/></svg>mara@kernelmail.org</li>
        <li><svg class="ico" viewBox="0 0 8 8"><circle cx="4" cy="4" r="4" fill="var(--blue)"/></svg>www.website.com</li>
        <li><svg class="ico" viewBox="0 0 8 8"><path d="M0 1h8v6H0z M0 1l4 3 4-3" fill="none" stroke="var(--blue)"/></svg>00 Dummy Text Road</li>
        <li style="padding-left:11px">Dummy 0000, Country</li>
      </ul>
    </div>
    <div class="corner-mark" role="img" aria-label="Brand symbol decoration"></div>
    <div class="band bottom"><span class="b-ink"></span><span class="b-blue"></span><span class="b-yellow"></span><span class="b-ink"></span></div>
  </section>

  <section class="sheet card-front" aria-label="Business card front">
    <div class="corner-mark top" role="img" aria-label="Brand symbol decoration"></div>
    <div class="ident">
      <div class="brand"><span class="brand-dot"></span>KERNEL</div>
      <ul class="contact">
        <li>Kernel Founders Academy</li>
        <li><svg class="ico" viewBox="0 0 8 8"><circle cx="4" cy="4" r="4" fill="var(--blue)"/></svg>www.website.com</li>
        <li><svg class="ico" viewBox="0 0 8 8"><path d="M0 1h8v6H0z M0 1l4 3 4-3" fill="none" stroke="var(--blue)"/></svg>00 Dummy Text Road</li>
        <li style="padding-left:11px">Dummy 0000, Country</li>
      </ul>
    </div>
  </section>

  <section class="sheet card-back" aria-label="Business card back">
    <div class="corner-mark" role="img" aria-label="White brand symbol decoration"></div>
    <div class="holder">
      <p class="holder-name">Mara Lind</p>
      <p class="holder-role">Managing Director</p>
    </div>
    <ul class="contact">
      <li><svg class="ico" viewBox="0 0 8 8"><rect x="2" y="0" width="4" height="8" rx="1" fill="#fff"/></svg>0-000-000-0000</li>
      <li><svg class="ico" viewBox="0 0 8 8"><rect x="0" y="1" width="8" height="6" fill="#fff"/></svg>mara@kernelmail.org</li>
    </ul>
  </section>

</body>
</html>
```